New Business card design to reflect rebrand

I would like a business card design with a good base colour for our new logo and also a placeholder for a profile pic of the card holder. the design needs to be editable to the point that we can easily change the picture of the person and use that design for printlarkly etc. we are looking at a metalic finish business card so will need a good base colour to bring out the finish.

Target Market(s)

prospective customers

Industry/Entity Type

Business

Contact Information for Business Card

I would like one editable design that we can change the name of the card holder and profile picture. The design need to be in a format that be send to printlarkly etc.

Our address is Fenwick Lodge, Mill Lane, Hartley Wintney, KT14 3WB Tel no. 01632 960418

Requirements
Must have
• place holder for a profile pic for the card holder. in AI or preferably PSD format

```html
<!DOCTYPE html>
<html lang="en">
<head>
<meta charset="utf-8">
<title>Brightvale Workplace Services – Business Card</title>
<link rel="stylesheet" href="https://fonts.googleapis.com/css2?family=Montserrat:wght@500;700&family=Questrial&display=swap">
<style>
  :root {
    --navy: #233a5c;
    --navy-deep: #1a2d4a;
    --navy-light: #2f4a70;
    --orange: #f26b21;
    --silver-1: #f2f3f4;
    --silver-2: #d5d8db;
    --silver-3: #bfc3c7;
    --ink: #3d4b5f;
    --backdrop: #e9e9e7;
  }
  * { box-sizing: border-box; margin: 0; padding: 0; }
  html, body { width: 1200px; height: 784px; overflow: hidden; }
  body {
    background: var(--backdrop);
    font-family: "Questrial", "Century Gothic", sans-serif;
    position: relative;
  }
  .card {
    position: absolute;
    top: 235px;
    width: 550px;
    height: 314px;
    border-radius: 4px;
    overflow: hidden;
    box-shadow: 0 6px 18px rgba(0,0,0,.18);
  }

  /* Back side */
  .card--back {
    left: 40px;
    background:
      linear-gradient(120deg, transparent 0 38%, rgba(255,255,255,.05) 38% 62%, transparent 62%),
      repeating-linear-gradient(180deg, rgba(255,255,255,.03) 0 1px, transparent 1px 3px),
      linear-gradient(160deg, var(--navy-light), var(--navy-deep));
    display: flex;
    align-items: center;
    justify-content: center;
  }
  .back-brand {
    font-family: "Montserrat", sans-serif;
    font-weight: 700;
    font-size: 58px;
    letter-spacing: 2px;
    color: #3a5580;
  }

  /* Front side */
  .card--front {
    left: 610px;
    background:
      repeating-linear-gradient(180deg, rgba(255,255,255,.35) 0 1px, transparent 1px 3px),
      linear-gradient(135deg, var(--silver-1), var(--silver-2) 55%, var(--silver-3));
  }
  .holder {
    position: absolute;
    top: 18px;
    right: 22px;
    text-align: right;
  }
  .holder__name {
    font-family: "Montserrat", sans-serif;
    font-weight: 500;
    font-size: 15px;
    color: var(--orange);
  }
  .holder__role {
    font-size: 10px;
    color: var(--navy);
    margin-top: 2px;
  }
  .brand {
    position: absolute;
    top: 70px;
    left: 26px;
    display: flex;
    align-items: center;
    gap: 10px;
  }
  .brand__dot {
    width: 16px;
    height: 16px;
    background: var(--orange);
    border-radius: 50%;
    flex: none;
  }
  .brand__name {
    font-family: "Montserrat", sans-serif;
    font-weight: 700;
    font-size: 26px;
    line-height: 1.05;
    color: var(--navy);
    text-transform: uppercase;
  }
  .brand__name span { display: block; font-size: 15px; letter-spacing: 3px; }
  .contacts {
    position: absolute;
    left: 26px;
    top: 158px;
    list-style: none;
  }
  .contacts li {
    display: flex;
    align-items: center;
    gap: 7px;
    font-size: 13.5px;
    color: var(--ink);
    height: 17px;
  }
  .contacts svg { width: 12px; height: 12px; fill: var(--orange); flex: none; }
  .portrait {
    position: absolute;
    right: 18px;
    top: 60px;
    width: 168px;
    height: 192px;
    background: linear-gradient(180deg, #b9bcc2, #6f6a78);
  }
  .stripe {
    position: absolute;
    left: 0; right: 0;
    top: 252px;
    height: 5px;
    background: var(--orange);
  }
  .band {
    position: absolute;
    left: 0; right: 0;
    top: 257px;
    bottom: 0;
    background: var(--navy);
  }
</style>
</head>
<body>

<section class="card card--back" aria-label="Card back">
  <div class="back-brand">Brightvale</div>
</section>

<section class="card card--front" aria-label="Card front">
  <div class="holder">
    <p class="holder__name">Dana Morell VP</p>
    <p class="holder__role">Manager</p>
  </div>

  <div class="brand">
    <span class="brand__dot"></span>
    <p class="brand__name">Brightvale<span>Workplace Services</span></p>
  </div>

  <ul class="contacts">
    <li><svg viewBox="0 0 12 12"><rect x="3" y="0" width="6" height="12" rx="1"/></svg>972-555-0183</li>
    <li><svg viewBox="0 0 12 12"><path d="M2 1l2.5-.5 1.5 3-1.5 1a7 7 0 003 3l1-1.5 3 1.5-.5 2.5C5 11 1 7 2 1z"/></svg>972-555-0129</li>
    <li><svg viewBox="0 0 12 12"><path d="M0 2h12v8H0z M0 2l6 4 6-4" stroke="#fff" stroke-width="1"/></svg>dana@brightvaleworkplace.com</li>
    <li><svg viewBox="0 0 12 12"><circle cx="6" cy="6" r="6"/><path d="M0 6h12M6 0v12" stroke="#fff" stroke-width="1"/></svg>www.brightvaleworkplace.com</li>
    <li><svg viewBox="0 0 12 12"><path d="M6 0a4 4 0 014 4c0 3-4 8-4 8S2 7 2 4a4 4 0 014-4z"/><circle cx="6" cy="4" r="1.5" fill="#fff"/></svg>4418 Harlan Ave. Plano, TX 75093</li>
  </ul>

  <div class="band"></div>
  <div class="stripe"></div>
  <div class="portrait" role="img" aria-label="Profile photo of the card holder"></div>
</section>

</body>
</html>
```